Certified Public Accountant specializing in tax preparation.

I need a business card designed that conveys knowledgeability, trustworthiness and competency. I am a licensed CPA and hold a Master's in taxation. As this is a personal service business, I would like to include my picture on the card.

```html
<!DOCTYPE html>
<html lang="en">
<head>
<meta charset="utf-8">
<title>Laura Whitcombe – Business Card</title>
<link rel="stylesheet" href="https://fonts.googleapis.com/css2?family=Arimo:wght@400;700&display=swap">
<style>
  :root {
    --backdrop: #d8d4cf;
    --card: #ffffff;
    --band: #e6e6e6;
    --name: #4a2a25;
    --title: #5b3d37;
    --contact: #1c1c1c;
    --credential: #4a2a25;
    --portrait-light: #e8c7b4;
    --portrait-mid: #9b6a55;
    --portrait-dark: #4b332c;
  }
  * { margin: 0; padding: 0; box-sizing: border-box; }
  html, body {
    width: 1200px;
    height: 791px;
    overflow: hidden;
    background: var(--backdrop);
    font-family: "Arimo", Arial, sans-serif;
  }
  .business-card {
    position: absolute;
    left: 160px;
    top: 145px;
    width: 880px;
    height: 500px;
    background: var(--card);
    border-radius: 26px;
    overflow: hidden;
    box-shadow: 0 4px 10px rgba(0,0,0,0.25);
  }
  .info-band {
    position: absolute;
    left: 0;
    top: 121px;
    width: 100%;
    height: 268px;
    background: var(--band);
  }
  .portrait {
    position: absolute;
    left: 129px;
    top: 113px;
    width: 286px;
    height: 286px;
    border-radius: 50%;
    border: 4px solid var(--card);
    background: radial-gradient(circle at 50% 45%, var(--portrait-light) 0%, var(--portrait-mid) 45%, var(--portrait-dark) 100%);
  }
  .details {
    position: absolute;
    left: 459px;
    top: 158px;
  }
  .name {
    font-size: 33px;
    font-weight: 700;
    letter-spacing: 0.5px;
    color: var(--name);
    line-height: 1;
  }
  .degree {
    margin-top: 4px;
    font-size: 22px;
    color: var(--title);
    line-height: 1.1;
  }
  .contact-list {
    list-style: none;
    margin-top: 22px;
    font-size: 20px;
    color: var(--contact);
    line-height: 25px;
  }
  .credential {
    margin-top: 16px;
    font-size: 19px;
    font-weight: 700;
    color: var(--credential);
  }
</style>
</head>
<body>
  <main class="business-card">
    <div class="info-band"></div>
    <div class="portrait" role="img" aria-label="Portrait photograph of the accountant"></div>
    <section class="details">
      <h1 class="name">LAURA WHITCOMBE</h1>
      <p class="degree">MASTER'S IN TAXATION</p>
      <ul class="contact-list">
        <li class="phone">555-210-4871</li>
        <li class="email">laura@ledgerline.com</li>
        <li class="website">www.ledgerline.com</li>
      </ul>
      <p class="credential">Licensed CPA</p>
    </section>
  </main>
</body>
</html>
```